Proposal Template Design

We are looking to have our proposal templates redesigned. attached are examples of what we have been using. as well as our current logo

```html
<!DOCTYPE html>
<html lang="en">
<head>
<meta charset="utf-8">
<title>Keystone Thermal Works – Proposal Template</title>
<link rel="stylesheet" href="https://fonts.googleapis.com/css2?family=Open+Sans:wdth,wght@75..100,400..800&family=Roboto+Condensed:wght@500;700&display=swap">
<style>
  :root{
    --backdrop:#8a8b8a;
    --paper:#ffffff;
    --brand-blue:#1c5fae;
    --brand-navy:#0b1a2c;
    --brand-black:#02070c;
    --sky:#5aa6e0;
    --rule:#7fb3e3;
    --ink:#000000;
    --body-text:#3a3a3a;
    --photo-light:#eeede8;
    --photo-mid:#d6d8d6;
    --photo-shade:#a9adad;
  }
  *{box-sizing:border-box;margin:0;padding:0}
  html,body{width:1003px;height:1200px;overflow:hidden;background:var(--backdrop)}
  body{position:relative;font-family:"Open Sans",Arial,sans-serif}

  .page{position:absolute;width:398px;height:516px;background:var(--paper);overflow:hidden}
  .page--cover{left:516px;top:62px}
  .page--intro{left:88px;top:622px}
  .page--body{left:516px;top:622px}

  .page__art{position:absolute;left:0;top:0;width:398px;height:516px}

  .brand-name{position:absolute;left:28px;top:18px;width:128px;
    font-family:"Open Sans",Arial,sans-serif;font-stretch:75%;font-weight:800;
    font-size:17px;line-height:18px;color:var(--brand-navy);letter-spacing:-0.2px}

  .services{position:absolute;top:69px;display:flex;align-items:center;gap:4px;
    font-family:"Roboto Condensed",Arial Narrow,sans-serif;font-weight:500;font-size:7.4px;
    letter-spacing:0.1px;text-transform:uppercase;white-space:nowrap}
  .services__sep{color:var(--sky);font-weight:400}
  .page--cover .services{left:218px;color:var(--brand-blue)}
  .page--intro .services,.page--body .services{left:217px;color:var(--ink)}

  .contact{position:absolute;list-style:none;font-family:"Open Sans",Arial,sans-serif;font-stretch:75%}
  .contact li{display:flex;align-items:center;white-space:nowrap}
  .contact svg{flex:none}
  .contact--cover{left:162px;top:461px;font-weight:700;font-size:10.4px;line-height:12.6px;color:var(--ink)}
  .contact--cover svg{width:6px;height:6px;margin-right:8px}
  .contact--header{left:262px;top:14px;font-weight:600;font-size:7.2px;line-height:11.8px;color:var(--sky)}
  .contact--header svg{width:5px;height:5px;margin-right:7px}

  .cover-title{position:absolute;left:50px;top:226px;font-stretch:75%;font-weight:700;
    font-size:40px;line-height:42px;color:var(--brand-blue);letter-spacing:-0.2px}
  .cover-date{position:absolute;left:51px;top:318px;font-stretch:75%;font-weight:700;
    font-size:24.5px;line-height:28px;color:var(--ink)}

  .hero-photo{position:absolute;left:0;top:86px;width:398px;height:200px;
    background:linear-gradient(120deg,var(--photo-light) 0%,var(--photo-mid) 55%,var(--photo-shade) 100%)}

  .section-title{position:absolute;left:28px;top:300px;font-stretch:75%;font-weight:700;
    font-size:16.5px;line-height:20px;color:var(--brand-blue)}
  .intro-copy{position:absolute;left:28px;top:333px;width:346px}
  .copy p{font-size:7.95px;line-height:10.6px;color:var(--body-text);margin-bottom:8px}

  .two-col{position:absolute;left:28px;top:108px;width:344px;height:370px;
    column-count:2;column-gap:9px;column-fill:auto;overflow:hidden}

  .footer-band{position:absolute;left:0;bottom:0;width:398px;height:9px;background:var(--brand-blue)}
</style>
</head>
<body>

<section class="page page--cover">
  <svg class="page__art" viewBox="0 0 398 516" aria-hidden="true">
    <defs>
      <linearGradient id="cover-head" x1="0" y1="0" x2="1" y2="0">
        <stop offset="0.15" stop-color="#1c5fae"/>
        <stop offset="0.55" stop-color="#0f3766"/>
        <stop offset="1" stop-color="#02070c"/>
      </linearGradient>
      <linearGradient id="cover-wedge" x1="1" y1="0" x2="0.4" y2="0.6">
        <stop offset="0" stop-color="#02070c"/>
        <stop offset="0.5" stop-color="#1c5fae"/>
        <stop offset="1" stop-color="#1c5fae"/>
      </linearGradient>
      <linearGradient id="cover-foot" x1="0" y1="1" x2="0.5" y2="0.3">
        <stop offset="0" stop-color="#02070c"/>
        <stop offset="0.6" stop-color="#1c5fae"/>
      </linearGradient>
    </defs>
    <polygon points="154,0 398,0 398,63 214,63 210,84 168,84 186,42" fill="url(#cover-head)"/>
    <line x1="0" y1="84.5" x2="398" y2="84.5" stroke="var(--rule)" stroke-width="0.8"/>
    <polygon points="209,85 398,85 398,355" fill="url(#cover-wedge)"/>
    <polygon points="0,374 101,516 0,516" fill="url(#cover-foot)"/>
  </svg>
  <div class="brand-name">Keystone Thermal Works</div>
  <nav class="services">
    <span>Spray Foam</span><span class="services__sep">|</span>
    <span>Fiberglass</span><span class="services__sep">|</span>
    <span>Insulation</span><span class="services__sep">|</span>
    <span>Roofing</span>
  </nav>
  <h1 class="cover-title">Proposal Tittle<br>Loremipsumdolor</h1>
  <p class="cover-date">September 2022</p>
  <ul class="contact contact--cover">
    <li><svg viewBox="0 0 10 10"><circle cx="5" cy="5" r="5" fill="var(--brand-blue)"/><circle cx="5" cy="4.3" r="1.8" fill="#fff"/></svg>P.O Box 218, Alden Ridge Texas 75011</li>
    <li><svg viewBox="0 0 10 10"><circle cx="5" cy="5" r="5" fill="var(--brand-blue)"/><path d="M3 3.2l1-.6.8 1.4-.6.5a3 3 0 0 0 1.3 1.3l.5-.6 1.4.8-.6 1c-2 .2-4-1.8-3.8-3.8z" fill="#fff"/></svg>555-014-2276</li>
    <li><svg viewBox="0 0 10 10"><circle cx="5" cy="5" r="5" fill="var(--brand-blue)"/><rect x="2.6" y="3.3" width="4.8" height="3.4" fill="#fff"/><path d="M2.6 3.3L5 5.2l2.4-1.9" stroke="var(--brand-blue)" stroke-width="0.6" fill="none"/></svg>@keystonethermal.com</li>
  </ul>
</section>

<section class="page page--intro">
  <svg class="page__art" viewBox="0 0 398 516" aria-hidden="true">
    <defs>
      <linearGradient id="intro-head" x1="0" y1="0" x2="1" y2="0">
        <stop offset="0.15" stop-color="#1c5fae"/>
        <stop offset="0.55" stop-color="#0f3766"/>
        <stop offset="1" stop-color="#02070c"/>
      </linearGradient>
      <linearGradient id="intro-bar" x1="0" y1="0" x2="1" y2="0">
        <stop offset="0" stop-color="#5aa6e0"/>
        <stop offset="1" stop-color="#1c5fae"/>
      </linearGradient>
    </defs>
    <polygon points="155,0 398,0 398,63 215,63 211,85 168,85 187,42" fill="url(#intro-head)"/>
    <polygon points="28,68 168,68 166,76 28,76" fill="url(#intro-bar)"/>
    <line x1="0" y1="85.5" x2="398" y2="85.5" stroke="var(--rule)" stroke-width="0.8"/>
  </svg>
  <div class="brand-name">Keystone Thermal Works</div>
  <ul class="contact contact--header">
    <li><svg viewBox="0 0 10 10"><circle cx="5" cy="5" r="5" fill="var(--sky)"/><circle cx="5" cy="4.3" r="1.8" fill="#0f3766"/></svg>P.O Box 218, Alden Ridge Texas 75011</li>
    <li><svg viewBox="0 0 10 10"><circle cx="5" cy="5" r="5" fill="var(--sky)"/><path d="M3 3.2l1-.6.8 1.4-.6.5a3 3 0 0 0 1.3 1.3l.5-.6 1.4.8-.6 1c-2 .2-4-1.8-3.8-3.8z" fill="#0f3766"/></svg>555-014-2276</li>
    <li><svg viewBox="0 0 10 10"><circle cx="5" cy="5" r="5" fill="var(--sky)"/><rect x="2.6" y="3.3" width="4.8" height="3.4" fill="#0f3766"/></svg>@keystonethermal.com</li>
  </ul>
  <nav class="services">
    <span>Spray Foam</span><span class="services__sep">|</span>
    <span>Fiberglass</span><span class="services__sep">|</span>
    <span>Insulation</span><span class="services__sep">|</span>
    <span>Roofing</span>
  </nav>
  <div class="hero-photo" role="img" aria-label="Photo of an installer in a white protective suit spraying foam insulation in an attic"></div>
  <h2 class="section-title">Tittle Headline Loremipsumdolor</h2>
  <div class="intro-copy copy">
    <p>Lorem ipsum dolor sit amet, consectetur adipiscing elit. Praesent ut lobortis est, at laoreet leo. Aliquam posuere placerat elementum. Pellentesque et ornare risus. Vestibulum blandit arcu nisi, elementum blandit elit facilisis a. Duis molestie malesuada condimentum. Proin auctor blandit diam vestibulum dapibus. Proin laoreet pellentesque felis, at fermentum neque sagittis ut. Duis gravida est vitae purus mollis laoreet.</p>
    <p>Pellentesque sagittis auctor sapien, vel rhoncus libero commodo et. Nullam in imperdiet ligula, eu mollis erat. In hac habitasse platea dictumst. Aliquam ligula mi, posuere vitae sem ut, vestibulum commodo dui. Integer commodo, metus vehicula laoreet interdum, odio felis condimentum metus, in pretium sem risus quis arcu. In eget nisl tempus arcu scelerisque pulvinar et sit amet magna. Lorem ipsum dolor sit amet, consectetur adipiscing elit. Praesent turpis neque, tincidunt vel ante vel, pellentesque porttitor dui. Maecenas pellentesque commodo elit et iaculis.</p>
  </div>
  <div class="footer-band"></div>
</section>

<section class="page page--body">
  <svg class="page__art" viewBox="0 0 398 516" aria-hidden="true">
    <defs>
      <linearGradient id="body-head" x1="0" y1="0" x2="1" y2="0">
        <stop offset="0.15" stop-color="#1c5fae"/>
        <stop offset="0.55" stop-color="#0f3766"/>
        <stop offset="1" stop-color="#02070c"/>
      </linearGradient>
      <linearGradient id="body-bar" x1="0" y1="0" x2="1" y2="0">
        <stop offset="0" stop-color="#5aa6e0"/>
        <stop offset="1" stop-color="#1c5fae"/>
      </linearGradient>
    </defs>
    <polygon points="154,0 398,0 398,63 214,63 210,85 167,85 186,42" fill="url(#body-head)"/>
    <polygon points="28,68 168,68 166,76 28,76" fill="url(#body-bar)"/>
    <line x1="0" y1="85.5" x2="398" y2="85.5" stroke="var(--rule)" stroke-width="0.8"/>
  </svg>
  <div class="brand-name">Keystone Thermal Works</div>
  <ul class="contact contact--header">
    <li><svg viewBox="0 0 10 10"><circle cx="5" cy="5" r="5" fill="var(--sky)"/><circle cx="5" cy="4.3" r="1.8" fill="#0f3766"/></svg>P.O Box 218, Alden Ridge Texas 75011</li>
    <li><svg viewBox="0 0 10 10"><circle cx="5" cy="5" r="5" fill="var(--sky)"/><path d="M3 3.2l1-.6.8 1.4-.6.5a3 3 0 0 0 1.3 1.3l.5-.6 1.4.8-.6 1c-2 .2-4-1.8-3.8-3.8z" fill="#0f3766"/></svg>555-014-2276</li>
    <li><svg viewBox="0 0 10 10"><circle cx="5" cy="5" r="5" fill="var(--sky)"/><rect x="2.6" y="3.3" width="4.8" height="3.4" fill="#0f3766"/></svg>@keystonethermal.com</li>
  </ul>
  <nav class="services">
    <span>Spray Foam</span><span class="services__sep">|</span>
    <span>Fiberglass</span><span class="services__sep">|</span>
    <span>Insulation</span><span class="services__sep">|</span>
    <span>Roofing</span>
  </nav>
  <div class="two-col copy">
    <p>Nulla varius eros suscipit, sodales metus at, pretium ipsum. Donec vulputate, justo eget vestibulum fringilla, tellus diam varius dui, ac rhoncus ante velit eu dolor. Vestibulum eget urna in elit dignissim luctus vel et nunc. Proin erat orci, iaculis eget nunc in, hendrerit egestas metus. Duis molestie sagittis metus sed cursus. Curabitur mollis mi et euismod vehicula. Nam tincidunt aliquam nunc a ornare. Suspendisse vestibulum laoreet felis bibendum placerat. Integer quam justo, consequat in erat vel, venenatis auctor magna. Donec a leo ut felis congue dictum. Etiam neque leo, tincidunt id ipsum sit amet, euismod rutrum nunc. Vivamus at libero orci.</p>
    <p>Proin commodo dictum dui. Proin venenatis turpis ac nunc auctor, et suscipit ipsum efficitur. Mauris vulputate neque nec est placerat, ac pharetra metus interdum. Pellentesque vitae nisl semper, vehicula nisi in, gravida massa. Nunc justo ipsum, convallis ut augue in, interdum pretium tortor. Praesent pharetra semper augue ac euismod. Ut non lectus euismod, vehicula ante at, sollicitudin risus. In hac habitasse platea dictumst. In congue elit mi, et dictum risus pulvinar in.</p>
    <p>Integer luctus tellus dui. Nulla eget neque sed massa semper lacinia eu id tortor. Etiam lacinia, nulla sed sodales porttitor, orci quam blandit nulla, nec ultricies ipsum nibh quis ligula. Ut dignissim ac est rutrum iaculis. Donec aliquam ex eu dignissim tristique. Cras ullamcorper porta non sed sem. Etiam eget ex sed ipsum aliquet elementum vel ve.</p>
    <p>Lorem ipsum dolor sit amet, consectetur adipiscing elit. Praesent ut lobortis est, at laoreet leo. Aliquam posuere placerat elementum. Pellentesque et ornare risus. Vestibulum blandit arcu nisi, elementum blandit elit facilisis a. Duis molestie malesuada condimentum. Proin auctor blandit diam vestibulum dapibus. Proin laoreet pellentesque felis, at fermentum neque sagittis ut. Duis gravida est vitae purus mollis laoreet.</p>
    <p>Pellentesque sagittis auctor sapien, vel rhoncus libero commodo et. Nullam in imperdiet ligula, eu mollis erat. In hac habitasse platea dictumst. Aliquam ligula mi, posuere vitae sem ut, vestibulum commodo dui. Integer commodo, metus vehicula laoreet interdum, odio felis condimentum metus, in pretium sem risus quis arcu. In eget nisl tempus arcu scelerisque pulvinar et sit amet magna. Lorem ipsum dolor sit amet, consectetur adipiscing elit. Praesent turpis neque, tincidunt vel ante vel, pellentesque porttitor dui. Maecenas pellentesque commodo elit et iaculis.</p>
    <p>Nulla varius eros suscipit, sodales metus at, pretium ipsum. Donec vulputate, justo eget vestibulum fringilla, tellus diam varius dui, ac rhoncus ante velit eu dolor. Vestibulum eget urna in elit dignissim luctus vel et nunc. Proin</p>
  </div>
  <div class="footer-band"></div>
</section>

</body>
</html>
```